A Flyer for a clinic/hospital waiting room to warn about patients that they must not abuse our staff

we need a flyer (text attached) with a background of a female nurse or medical doctor photo. I like the example photo where there are four headless satff lined up - something like this, indicating that we are a team and will not tolerate abuse
A4
the text will be over the photo.

Target Market(s)

patients who come to our clinic

Industry/Entity Type

medicine - urology

Colors
0054AA
0677BA
7BADD7
CADEEF
E8F1F8
0094D4
00A9DD
6FCCEA
C7EBF8
E9F6FB

Requirements
Must have
• a photo taking up the whole A4, and text over this. The photos I haev sent are just examples - I will need yo to source a photo
Nice to have
• Horizontal A4 and vertical A4 options. Please add our logo in small , in the bottom right corner

```html
<!DOCTYPE html>
<html lang="en">
<head>
<meta charset="UTF-8">
<title>Zero-Tolerance for Aggressive Behaviour – Southgate Urology</title>
<link href="https://fonts.googleapis.com/css2?family=Montserrat:wght@500;600;700;800;900&family=Roboto:wght@400;500&family=Lora:ital,wght@1,500&display=swap" rel="stylesheet">
<style>
  :root{
    --red:#e8202a;
    --navy:#24398c;
    --ink:#111111;
    --band-top:#0c2b72;
    --band-bottom:#1a4aa6;
    --strip:#0aa6e4;
    --yellow:#ffe11a;
    --white:#ffffff;
    --rule:#4d88d6;
    --brand-blue:#0677BA;
  }
  *{margin:0;padding:0;box-sizing:border-box;}
  html,body{width:1200px;height:848px;overflow:hidden;background:#ffffff;}
  .flyer{position:relative;width:1200px;height:848px;overflow:hidden;font-family:'Roboto',Arial,sans-serif;}

  .hero-photo{
    position:absolute;left:0;top:0;width:1200px;height:552px;
    background:
      linear-gradient(90deg, rgba(238,244,249,0.96) 0%, rgba(226,236,245,0.9) 40%, rgba(210,226,238,0.35) 52%, rgba(0,0,0,0) 60%),
      linear-gradient(100deg, #dbe6ef 0%, #cfdde9 45%, #3aa3c4 62%, #2496b8 78%, #1f8aaf 100%);
  }

  .brand-tab{
    position:absolute;left:160px;top:0;width:305px;height:187px;
    background:var(--white);border-radius:0 0 24px 24px;
    display:flex;flex-direction:column;align-items:center;justify-content:center;gap:14px;
  }
  .brand-dot{width:54px;height:54px;border-radius:50%;background:var(--brand-blue);}
  .brand-name{font-family:'Montserrat',Arial,sans-serif;font-weight:500;font-size:27px;color:#3a3f48;letter-spacing:-0.2px;}

  .headline{position:absolute;left:20px;width:620px;top:214px;text-align:center;font-family:'Montserrat',Arial,sans-serif;}
  .headline .lead{font-weight:700;font-size:32px;line-height:38px;color:var(--ink);}
  .headline .lead .accent{color:var(--red);font-weight:800;}
  .headline .big{font-weight:900;font-size:82px;line-height:80px;letter-spacing:-1px;}
  .headline .big.red{color:var(--red);margin-top:10px;}
  .headline .big.navy{color:var(--navy);}

  .tagline{position:absolute;left:20px;width:620px;top:446px;text-align:center;font-family:'Lora',Georgia,serif;font-style:italic;font-weight:500;font-size:26px;line-height:34px;}
  .tagline .red{color:var(--red);}
  .tagline .dark{color:var(--ink);}

  .info-band{position:absolute;left:0;top:550px;width:1200px;height:281px;background:linear-gradient(180deg,var(--band-top) 0%,var(--band-bottom) 100%);}
  .base-strip{position:absolute;left:0;top:831px;width:1200px;height:17px;background:var(--strip);}

  .definition{position:absolute;left:50px;top:580px;width:520px;color:var(--white);}
  .definition-head{display:flex;align-items:flex-start;gap:10px;}
  .definition-head svg{flex:none;margin-top:2px;}
  .definition-title{font-family:'Montserrat',Arial,sans-serif;font-weight:700;font-size:18px;line-height:20px;color:var(--yellow);}
  .definition-list{list-style:none;margin-top:9px;}
  .definition-list li{font-size:18.5px;line-height:24.5px;}
  .definition-list li::before{content:"•";color:var(--yellow);margin-right:6px;}

  .divider-v{position:absolute;width:1px;background:var(--rule);}
  .divider-main{left:578px;top:578px;height:218px;}
  .divider-sub{left:873px;top:680px;height:116px;}
  .divider-h{position:absolute;left:628px;top:678px;width:521px;height:1px;background:var(--rule);}
  .divider-node{position:absolute;left:868px;top:673px;width:11px;height:11px;border-radius:50%;border:1.5px solid var(--rule);background:var(--band-top);}

  .policy{position:absolute;color:var(--white);font-size:16px;line-height:20.5px;}
  .policy-main{left:628px;top:578px;width:540px;}
  .policy-support{left:628px;top:699px;width:230px;}
  .policy-reason{left:901px;top:699px;width:250px;}
</style>
</head>
<body>
<div class="flyer">
  <div class="hero-photo" role="img" aria-label="Photo of a nurse in teal scrubs with a stethoscope, arms crossed, against a soft blurred clinic background"></div>

  <div class="brand-tab">
    <span class="brand-dot"></span>
    <span class="brand-name">Southgate Urology</span>
  </div>

  <div class="headline">
    <p class="lead">We have <span class="accent">zero-tolerance</span></p>
    <p class="lead">for any form of</p>
    <p class="big red">AGGRESSIVE</p>
    <p class="big navy">BEHAVIOUR</p>
  </div>

  <div class="tagline">
    <p class="red">Our staff treat you with respect</p>
    <p class="dark">and we expect the same in return</p>
  </div>

  <div class="info-band"></div>
  <div class="base-strip"></div>

  <section class="definition">
    <div class="definition-head">
      <svg width="36" height="36" viewBox="0 0 36 36" aria-hidden="true">
        <circle cx="18" cy="18" r="16" fill="none" stroke="#ffffff" stroke-width="2.4"/>
        <path d="M10 18.5 L16 24 L28 9" fill="none" stroke="#ffffff" stroke-width="3" stroke-linecap="round" stroke-linejoin="round"/>
      </svg>
      <p class="definition-title">Aggressive behaviour<br>(in-person or on the telephone) is:</p>
    </div>
    <ul class="definition-list">
      <li>Verbal harassment</li>
      <li>Any verbal or physical confrontation</li>
      <li>Raising your voice or making unreasonable demands</li>
      <li>Abusive or intimidating behaviour</li>
      <li>Sexual or suggestive language or behaviour</li>
      <li>Making threats to our staff</li>
      <li>Swearing</li>
    </ul>
  </section>

  <div class="divider-v divider-main"></div>
  <div class="divider-h"></div>
  <div class="divider-node"></div>
  <div class="divider-v divider-sub"></div>

  <p class="policy policy-main">If any of our staff feel intimidated in any way, we will always support them. Incidents will result in your immediate removal from the facility, termination of your relationship with the practice, and may result in prosecution.</p>
  <p class="policy policy-support">In all circumstances we will support any staff member who wishes to press charges against a perpetrator of aggressive behaviour.</p>
  <p class="policy policy-reason">We take this stance because our staff work extremely hard in busy circumstances to help you and we will no longer tolerate any form of aggression or abuse.</p>
</div>
</body>
</html>
```